Flyer Design Project

We are a restaurant delivery service. We deliver from a variety of restaurants. We are looking for a small flyer that we will put on the front desk at a restaurant that says "We Deliver!" Include our website trovaloopcourier.com and phone number 833-9 Gem Lamp! We would like the emphasis to be on ordering online. The flyer size should be 4.25" x 5.5".

```html
<!DOCTYPE html>
<html lang="en">
<head>
<meta charset="utf-8">
<title>Trovaloop Courier – We Deliver</title>
<link href="https://fonts.googleapis.com/css2?family=Montserrat:wght@500;800;900&family=Questrial&family=Lobster&display=swap" rel="stylesheet">
<style>
  :root {
    --brand-red: #b8232a;
    --band-red: #b62a2f;
    --ink: #111111;
    --paper: #ffffff;
    --key-dark: #2a2a2c;
    --key-silver: #d9dadc;
  }
  * { margin: 0; padding: 0; box-sizing: border-box; }
  html, body { width: 928px; height: 1200px; overflow: hidden; background: var(--paper); }
  .flyer { position: relative; width: 928px; height: 1200px; overflow: hidden; background: var(--paper); }

  .side-band {
    position: absolute; left: 0; top: 0; width: 164px; height: 1200px;
    background: var(--band-red);
    display: flex; align-items: center; justify-content: center;
  }
  .side-band__url {
    writing-mode: vertical-rl; transform: rotate(180deg);
    font-family: "Montserrat", sans-serif; font-weight: 900;
    font-size: 86px; letter-spacing: -1px; color: var(--paper);
    white-space: nowrap; line-height: 1;
    text-shadow: 3px -3px 6px rgba(0,0,0,0.35);
  }

  .hero-photo {
    position: absolute; left: 164px; top: 0; width: 764px; height: 482px;
    background:
      radial-gradient(ellipse 30% 22% at 68% 42%, #c2282d 0%, #9e1f24 70%, transparent 72%),
      linear-gradient(160deg, var(--key-dark) 0%, #3b3b3e 35%, var(--key-silver) 36%, #f2f2f3 60%, var(--key-dark) 61%, #1d1d1f 85%, var(--key-silver) 86%);
  }

  .headline {
    position: absolute; left: 202px; top: 552px; width: 700px;
    font-family: "Questrial", sans-serif; color: var(--ink);
    font-size: 42px; line-height: 66px;
  }
  .headline__accent {
    font-family: "Lobster", cursive; color: var(--brand-red);
    font-size: 68px; letter-spacing: 0.5px;
  }
  .tagline {
    position: absolute; left: 203px; top: 784px;
    font-family: "Questrial", sans-serif; font-size: 23px; color: var(--ink);
    letter-spacing: 0.2px;
  }
  .tagline em { font-style: normal; color: var(--brand-red); }

  .brand {
    position: absolute; left: 196px; top: 930px;
    display: flex; align-items: center; gap: 22px;
  }
  .brand__dot { width: 70px; height: 70px; border-radius: 50%; background: var(--brand-red); }
  .brand__name {
    font-family: "Montserrat", sans-serif; font-weight: 800;
    font-size: 60px; color: var(--brand-red); line-height: 1;
  }

  .contact {
    position: absolute; left: 348px; top: 1070px;
    font-family: "Montserrat", sans-serif; font-weight: 900;
    font-size: 30px; line-height: 40px; color: var(--ink);
  }
</style>
</head>
<body>
  <main class="flyer">
    <aside class="side-band">
      <span class="side-band__url">trovaloopcourier.com</span>
    </aside>

    <div class="hero-photo" role="img" aria-label="Close-up photo of a silver laptop keyboard with a red key showing a fork, plate and knife icon"></div>

    <h1 class="headline">
      We Bring Your <span class="headline__accent">Favorite</span><br>
      <span class="headline__accent">Restaurants</span> Right to<br>
      Your Front Door!
    </h1>
    <p class="tagline">YOUR NEXT MEAL IS ONLY A <em>“CLICK”</em> AWAY!</p>

    <div class="brand">
      <span class="brand__dot"></span>
      <span class="brand__name">Trovaloop Courier</span>
    </div>

    <p class="contact">
      WEB: trovaloopcourier.com<br>
      CALL: 833-9 GEM LAMP!
    </p>
  </main>
</body>
</html>
```